Asia Hotel need a card and logo

The new hotel in East Asia, Taiwan need a business card and logo design.The hotel's Chinese name is 岚柏文旅,English name is "Velmira Hotel".The core concept of this hotel is "Eco green", going to use many plant etc.,The building's first outlook draft is attached in the file for your reference.The style be modern and fashion will be good. Thank you.
Target Market(s)
East Asia
Industry/Entity Type
Hotel
Contact Information for Business Card
The hotel's name both in Chinese and English :岚柏商旅 Velmira Hotel
The logo, address, E-mail and tel number place.
Stuff's name and title.
Font styles to use
Colors
Designer to choose colors to be used in the design.
Look and feel
Each slider illustrates characteristics of the customer's brand and the style your logo design should communicate.

```html
<!DOCTYPE html>
<html lang="zh-Hant">
<head>
<meta charset="utf-8">
<title>岚柏商旅 Velmira Hotel — Business Card</title>
<link href="https://fonts.googleapis.com/css2?family=Noto+Sans+SC:wght@700&family=Source+Sans+3:wght@400;500&display=swap" rel="stylesheet">
<style>
  :root {
    --backdrop: #7fa9b8;
    --paper: #f5f5f5;
    --leaf: #c6cd2f;
    --charcoal: #333333;
    --ink: #111111;
    --rule: #555555;
    --white: #ffffff;
  }
  * { margin: 0; padding: 0; box-sizing: border-box; }
  html, body { width: 1200px; height: 1200px; overflow: hidden; }
  body {
    position: relative;
    background: var(--backdrop);
    font-family: "Source Sans 3", "Helvetica Neue", Arial, sans-serif;
  }
  .card {
    position: absolute;
    top: 224px;
    width: 404px;
    height: 705px;
    background: var(--paper);
    overflow: hidden;
  }
  .card--front { left: 98px; }
  .card--back { left: 674px; }

  .stripe { position: absolute; background: var(--leaf); }
  .card--front .stripe--left { left: 0; top: 0; width: 22px; height: 100%; }
  .card--front .stripe--right { right: 0; top: 0; width: 19px; height: 100%; }

  .brand {
    position: absolute;
    left: 0; right: 0;
    text-align: center;
    color: var(--ink);
  }
  .brand__zh {
    font-family: "Noto Sans SC", sans-serif;
    font-weight: 700;
    line-height: 1;
    letter-spacing: -1px;
  }
  .brand__en {
    font-family: "Source Sans 3", sans-serif;
    font-weight: 500;
    line-height: 1;
    margin-top: 6px;
    letter-spacing: -0.5px;
  }
  .card--front .brand { top: 282px; }
  .card--front .brand__zh { font-size: 62px; }
  .card--front .brand__en { font-size: 34px; }

  .card--back .band--top { left: 0; top: 0; width: 100%; height: 22px; }
  .card--back .band--bottom { left: 0; bottom: 0; width: 100%; height: 34px; }
  .card--back .brand { top: 112px; }
  .card--back .brand__zh { font-size: 62px; }
  .card--back .brand__en { font-size: 34px; }

  .person {
    position: absolute;
    left: 0; top: 333px;
    width: 100%; height: 84px;
    background: var(--leaf);
    color: var(--white);
    text-align: center;
    padding-top: 20px;
  }
  .person__name { font-size: 30px; font-weight: 400; line-height: 1; }
  .person__title { font-size: 19px; font-weight: 400; line-height: 1; margin-top: 2px; }

  .contacts {
    position: absolute;
    left: 0; top: 417px;
    width: 100%; height: 254px;
    background: var(--charcoal);
    list-style: none;
  }
  .contact {
    position: relative;
    height: 84.7px;
    display: flex;
    align-items: center;
    border-bottom: 1px solid var(--rule);
  }
  .contact:last-child { border-bottom: none; }
  .contact__icon {
    width: 76px;
    height: 100%;
    display: flex;
    align-items: center;
    justify-content: center;
    border-right: 1px solid #3a3a3a;
  }
  .contact__icon svg { width: 40px; height: 40px; display: block; }
  .contact__text {
    padding-left: 32px;
    color: var(--white);
    font-size: 14px;
    line-height: 1.45;
  }
  .contact__text--spaced { line-height: 1.6; }
</style>
</head>
<body>
  <section class="card card--front" aria-label="Card front">
    <div class="stripe stripe--left"></div>
    <div class="stripe stripe--right"></div>
    <div class="brand">
      <div class="brand__zh">岚柏商旅</div>
      <div class="brand__en">VELMIRA HOTEL</div>
    </div>
  </section>

  <section class="card card--back" aria-label="Card back">
    <div class="stripe band--top"></div>
    <div class="brand">
      <div class="brand__zh">岚柏商旅</div>
      <div class="brand__en">VELMIRA HOTEL</div>
    </div>
    <div class="person">
      <div class="person__name">JOHN SMITH</div>
      <div class="person__title">TITLE</div>
    </div>
    <ul class="contacts">
      <li class="contact">
        <span class="contact__icon">
          <svg viewBox="0 0 40 40" aria-hidden="true">
            <circle cx="20" cy="20" r="20" fill="#fff"/>
            <path d="M13 11c1-1 2.5-1 3.3.2l2 3c.6.9.3 2-.5 2.6l-1.2.9c.9 2.3 2.9 4.4 5.2 5.4l.9-1.2c.6-.8 1.8-1 2.6-.4l3 2c1.1.8 1.1 2.3.1 3.3l-1.3 1.3c-1.6 1.6-5.5.9-9.6-3.2S10.1 15.6 11.7 12z" fill="#333"/>
          </svg>
        </span>
        <p class="contact__text">+0 000 000 000<br>+0 000 000 000</p>
      </li>
      <li class="contact">
        <span class="contact__icon">
          <svg viewBox="0 0 40 40" aria-hidden="true">
            <circle cx="20" cy="20" r="20" fill="#fff"/>
            <rect x="11" y="14" width="18" height="12" fill="none" stroke="#333" stroke-width="2"/>
            <path d="M11 14l9 7 9-7M11 26l7-6M29 26l-7-6" fill="none" stroke="#333" stroke-width="1.6"/>
          </svg>
        </span>
        <p class="contact__text">JOHNSMITH@YOURMAIL.COM</p>
      </li>
      <li class="contact">
        <span class="contact__icon">
          <svg viewBox="0 0 40 40" aria-hidden="true">
            <circle cx="20" cy="20" r="20" fill="#fff"/>
            <path d="M20 9c-4.4 0-7.5 3.2-7.5 7.3 0 5.2 7.5 14.2 7.5 14.2s7.5-9 7.5-14.2C27.5 12.2 24.4 9 20 9z" fill="#333"/>
            <circle cx="20" cy="16.5" r="2.8" fill="#fff"/>
          </svg>
        </span>
        <p class="contact__text contact__text--spaced">YOUR FIRST ADDRESS LINE<br>YOUR SECOND ADDRESS LINE</p>
      </li>
    </ul>
    <div class="stripe band--bottom"></div>
  </section>
</body>
</html>
```